Wex2Legal Letterhead

Need a new letterhead for my law firm.
IDENTIFYING INFORMATION BELOW:
Teodoro R Galvani III
Attorney at Law
Address: 2834 Brackett Ave, Ste 300, Dallas, TX 75204
Phone: 877-642-7183
Fax: 469-538-2716
Email: ted@wex2legal-example.com
Website: www.wex2legal-example.com

Colors
0054AA
0677BA
7BADD7
CADEEF
E8F1F8

Requirements
Must have
• Logo needs to be on the letterhead, along with identifying information which is included in the project description.

```html
<!DOCTYPE html>
<html lang="en">
<head>
<meta charset="utf-8">
<title>Wex2Legal Letterhead</title>
<link href="https://fonts.googleapis.com/css2?family=Montserrat:wght@400;500;600&family=Kaushan+Script&display=swap" rel="stylesheet">
<style>
  :root {
    --ink: #1c1c1c;
    --text: #555a60;
    --blue: #1b9ad6;
    --paper: #fbfbfb;
    --backdrop: #e6e7e9;
  }
  * { margin: 0; padding: 0; box-sizing: border-box; }
  html, body {
    width: 1200px; height: 900px; overflow: hidden;
    background: var(--backdrop);
    font-family: "Montserrat", sans-serif;
  }
  .letterhead {
    position: absolute; left: 300px; top: 26px;
    width: 600px; height: 848px;
    background: var(--paper);
    box-shadow: 0 4px 18px rgba(0,0,0,0.12);
    overflow: hidden;
  }
  .top-band { position: absolute; left: 0; top: 0; width: 100%; height: 10px; background: var(--ink); }
  .top-rule { position: absolute; left: 0; top: 10px; width: 100%; height: 5px; background: var(--blue); }

  .brand { position: absolute; left: 40px; top: 86px; }
  .brand-row { display: flex; align-items: center; gap: 8px; }
  .brand-mark { width: 14px; height: 14px; background: var(--blue); flex: none; }
  .brand-name {
    font-size: 26px; font-weight: 600; color: var(--ink);
    letter-spacing: 0.5px; line-height: 1;
  }
  .brand-tagline {
    font-size: 9.5px; font-weight: 400; color: var(--ink);
    letter-spacing: 2.5px; margin-top: 6px; padding-left: 22px;
  }

  .contact { position: absolute; top: 54px; right: 34px; display: flex; gap: 14px; font-size: 8.5px; color: var(--text); line-height: 1.55; }
  .contact-address { display: flex; gap: 8px; padding-top: 14px; }
  .contact-divider { width: 1px; height: 52px; background: #9aa0a6; }
  .contact-lines { list-style: none; }
  .contact-lines li { display: flex; align-items: center; gap: 7px; }
  .icon { width: 9px; height: 9px; fill: var(--blue); flex: none; }

  .letter { position: absolute; left: 64px; top: 256px; width: 476px; color: var(--text); }
  .letter-date { font-size: 10px; font-weight: 500; }
  .recipient-name { margin-top: 24px; font-size: 12.5px; font-weight: 600; color: var(--blue); }
  .recipient-title { font-size: 10px; font-weight: 500; margin-top: 2px; }
  .salutation { margin-top: 32px; font-size: 10px; font-weight: 500; }
  .letter-body p { margin-top: 20px; font-size: 7.6px; line-height: 1.9; }
  .closing { margin-top: 56px; font-size: 10px; font-weight: 500; }
  .signature { font-family: "Kaushan Script", cursive; font-size: 24px; color: var(--blue); margin-top: 4px; }

  .website { position: absolute; left: 300px; bottom: 30px; font-size: 8.5px; font-weight: 600; color: var(--text); }
  .bottom-band { position: absolute; left: 0; bottom: 0; width: 100%; height: 8px; display: flex; }
  .bottom-band-blue { flex: 0 0 52%; background: var(--blue); }
  .bottom-band-dark { flex: 1; background: var(--ink); }
</style>
</head>
<body>
  <main class="letterhead">
    <div class="top-band"></div>
    <div class="top-rule"></div>

    <header class="brand">
      <div class="brand-row">
        <span class="brand-mark"></span>
        <span class="brand-name">Wex2Legal</span>
      </div>
      <div class="brand-tagline">DALLAS INJURY COUNSEL</div>
    </header>

    <section class="contact">
      <div class="contact-address">
        <svg class="icon" viewBox="0 0 10 10"><path d="M5 0a3.5 3.5 0 0 0-3.5 3.5C1.5 6 5 10 5 10s3.5-4 3.5-6.5A3.5 3.5 0 0 0 5 0zm0 5a1.4 1.4 0 1 1 0-2.8A1.4 1.4 0 0 1 5 5z"/></svg>
        <div>2834 Brackett Ave,<br>Ste 300, Dallas,<br>TX 75204</div>
      </div>
      <div class="contact-divider"></div>
      <ul class="contact-lines">
        <li><svg class="icon" viewBox="0 0 10 10"><path d="M2 0.5l1.8 2.2-1 1.1a6 6 0 0 0 3.4 3.4l1.1-1L9.5 8 8.3 9.5C4.3 9.3.7 5.7.5 1.7z"/></svg>877-642-7183</li>
        <li><svg class="icon" viewBox="0 0 10 10"><path d="M2.5 0h5v3h-5zM0 3.5h10V8H8v2H2V8H0zM3 6.5v2.5h4V6.5z"/></svg>469-538-2716</li>
        <li><svg class="icon" viewBox="0 0 10 10"><path d="M0 1.5h10v7H0zM1 2.5l4 3 4-3v-.3H1z" fill-rule="evenodd"/></svg>ted@wex2legal-example.com</li>
      </ul>
    </section>

    <article class="letter">
      <div class="letter-date">01 March, 2022</div>
      <div class="recipient-name">Teodoro R Galvani III</div>
      <div class="recipient-title">Attorney at Law</div>
      <div class="salutation">Dear Sir,</div>
      <div class="letter-body">
        <p>Teodoro R. Galvani, III, Attorney at Law, PLLC is a Texas personal injury law firm representing individuals who have been injured in accidents. We understand the ramifications an injury of any size can have on your life and are dedicated to assisting every one of our clients in obtaining the care and restitution they deserve.</p>
        <p>By concentrating his practice exclusively on protecting the rights of personal injury victims, Ted can use the experience and knowledge he's gained to enable him to provide his clients unparalleled representation. Every case that Ted handles receives his personal attention, and all initial consultations are provided free of charge. If Ted can't get you a settlement, his representation will cost you $0.00.</p>
        <p>Ted appreciates the stress and inconvenience a personal injury causes and understands the importance of being able to contact your attorney directly with your questions and concerns. Because of this, his client's have direct access to him 24 hours a day, 7 days a week, 365 days a year.</p>
        <p>If you have suffered a personal injury contact Teodoro R. Galvani III, Attorney at Law, PLLC for a free evaluation of your case. I'm available at your convenience - contact me online, or call 877-642-7183 for assistance 24/7/365.</p>
      </div>
      <div class="closing">Sencerly Yours</div>
      <div class="signature">Your Name</div>
    </article>

    <footer>
      <div class="website">www.wex2legal-example.com</div>
      <div class="bottom-band"><div class="bottom-band-blue"></div><div class="bottom-band-dark"></div></div>
    </footer>
  </main>
</body>
</html>
```